依頼詳細
不動産物件情報の冊子の表紙デザインです。5月らしいイメージと、簡単には捨てられないインパクトのあるデザインをお願いします。
会社WEB:http://morinaga-hoshizora.jp/
記載項目
タイトル「物件情報 2019 5月号」 会社ロゴ:添付参照
希望イメージ
シンプル 複雑
単色 カラフル
暗い 明るい
日常 高級
遊び心 厳粛
未来的 伝統的
女性的 男性的
希望する色
納品ファイル
• イラストレーター形式 (.ai)
補足説明
四半期に一度発行予定ですので、継続の可能性もあります
参考までに新春号のデータを添付いたします
先述の、物件情報は、関東・九州の情報が主ですが、全国の情報を掲載しております。
■ 選んだ理由

弊社の意図をよくご理解いただき、季節に合ったご提案をいただきました。データ化の対応も迅速な対応で、助かりました。引き続きよろしくお願いします

■ 提案者全員のお礼・コメント

たくさんのご提案をいただき、参加いただいた皆様には深謝いたします。
どのご提案も、素晴らしいものでした。

次号は夏ごろを予定しておりますので、その折には、また多くの方々のご提案をいただくことができればと存じます。
今後ともよろしくお願いいたします

```html
<!DOCTYPE html>
<html lang="ja">
<head>
<meta charset="utf-8">
<title>物件情報 2019 5月号</title>
<link rel="stylesheet" href="https://fonts.googleapis.com/css2?family=Noto+Sans+JP:wght@200;700&family=Montserrat:wght@400;600&display=swap">
<style>
  :root {
    --paper: #ffffff;
    --ink: #3a3a3a;
    --accent-blue: #2a7fd0;
    --sky-deep: #1f6fd1;
    --sky-mid: #6aa9ea;
    --sky-light: #d6e8f8;
    --logo-gold: #c9a227;
  }
  html, body { margin: 0; padding: 0; overflow: hidden; background: var(--paper); }
  .cover {
    position: relative;
    width: 851px;
    height: 1200px;
    overflow: hidden;
    background: var(--paper);
    font-family: "Noto Sans JP", sans-serif;
  }
  .sky-photo { position: absolute; inset: 0; }
  .tagline {
    position: absolute;
    left: 395px;
    top: 36px;
    margin: 0;
    font-size: 20px;
    font-weight: 700;
    color: var(--accent-blue);
    letter-spacing: 0.5px;
    white-space: nowrap;
  }
  .title {
    position: absolute;
    left: 50px;
    top: 118px;
    margin: 0;
    display: flex;
    font-size: 120px;
    font-weight: 200;
    line-height: 1;
    color: var(--ink);
  }
  .title-char { display: block; width: 120px; text-align: center; }
  .title-accent { color: var(--paper); font-weight: 700; }
  .brand {
    position: absolute;
    left: 655px;
    top: 160px;
    display: flex;
    align-items: center;
    gap: 8px;
    font-family: "Montserrat", sans-serif;
    font-size: 22px;
    font-weight: 600;
    color: var(--ink);
  }
  .brand-dot {
    width: 26px; height: 26px;
    border-radius: 50%;
    background: var(--logo-gold);
  }
  .issue {
    position: absolute;
    left: 580px;
    width: 220px;
    top: 790px;
    text-align: center;
    color: var(--paper);
    font-family: "Montserrat", sans-serif;
  }
  .issue-month { display: block; font-size: 200px; font-weight: 600; line-height: 1; }
  .issue-year { display: block; font-size: 54px; font-weight: 600; line-height: 1.1; margin-top: 8px; }
  .issue-vol { display: block; font-size: 28px; font-weight: 400; margin-top: 2px; }
</style>
</head>
<body>
<main class="cover">
  <svg class="sky-photo" width="851" height="1200" viewBox="0 0 851 1200" role="img" aria-label="青空と白い雲が映る窓ガラスの写真">
    <defs>
      <linearGradient id="sky" x1="0" y1="0" x2="0" y2="1">
        <stop offset="0" stop-color="#1f6fd1"/>
        <stop offset="0.45" stop-color="#6aa9ea"/>
        <stop offset="0.75" stop-color="#d6e8f8"/>
        <stop offset="1" stop-color="#6aa9ea"/>
      </linearGradient>
    </defs>
    <path d="M168 0 H300 V262 L851 232 V1200 H0 V290 L168 280 Z" fill="url(#sky)"/>
  </svg>

  <p class="tagline">関東・九州を中心とした全国の不動産を掲載！</p>
  <h1 class="title"><span class="title-char">物</span><span class="title-char title-accent">件</span><span class="title-char">情</span><span class="title-char">報</span></h1>

  <div class="brand"><span class="brand-dot"></span>Hoshizora</div>

  <div class="issue">
    <span class="issue-month">5</span>
    <span class="issue-year">2019</span>
    <span class="issue-vol">vol.003</span>
  </div>
</main>
</body>
</html>
```